Post Card Mailer for QUIK PATH PROSPECTS using new logo

We need a post card designed to send through the USA mail service that will go to new prospective clients.

The post card will introduce me and my new company and try to educate them our on company and services.

The goal is for them to call me or email me so I can have a discussion and try to sell our product.

Our product is a name list of individuals that are looking for consulting / help to determine if they qualify for USA social security benefits and then help to manage the process. We sell this name list to law firms that help these individuals.

Our services are better because we have a better less expensive way to identify people via the internet that want help. Our conversion rate is 15%, so every 100 leads a law firm buys the will obtain 15 customers / clients.
Updates

Designer on Logo took alot longer than expected. Also there were two projects that needed to combined into one. Which was done yesterday.

Went on vacation/holiday

Target Market(s)

Law firms

Font styles to use
Serif
Sans Serif
Script

Colors

Designer to choose colors to be used in the design.

Requirements
Must have
• The size of the mailer should be about 6 by 8 inches.
• Two sides.
• Side 1: With our Logo and key messages we want to communicate.
• Side 2: A space to be used by the USA mail services in lower right, my photo and an introduction by me to our company and why they should buy from my company.
Nice to have
• Images that represent what we do, how we help, and our target market.
Should not have
• Poor taste in images that upset people

```html
<!DOCTYPE html>
<html lang="en">
<head>
<meta charset="utf-8">
<title>Quik Path Prospects – Postcard Mailer</title>
<link href="https://fonts.googleapis.com/css2?family=Oswald:wght@400;500&family=Lato:wght@400;700&family=Arimo:wght@400;700&display=swap" rel="stylesheet">
<style>
:root{
  --navy:#1c2b45;
  --navy-deep:#111c30;
  --blue:#0c5fa8;
  --blue-bright:#1a86d4;
  --cyan:#27a7e6;
  --ink:#1a1a1a;
  --grey:#555a60;
  --paper:#ffffff;
  --stage:#e9ecef;
  --head:"Oswald", sans-serif;
  --body:"Lato", sans-serif;
}
*{box-sizing:border-box;margin:0;padding:0}
html,body{width:947px;height:1200px;overflow:hidden;background:var(--stage)}
.sheet{position:relative;width:947px;height:1200px}
.card-slot{position:absolute;left:93px;width:760px;height:572px}
.card-slot.front-slot{top:17px}
.card-slot.back-slot{top:611px}
.card{position:absolute;left:0;top:0;width:800px;height:602px;transform:scale(.95);transform-origin:0 0;overflow:hidden;background:var(--paper);box-shadow:0 4px 14px rgba(0,0,0,.25);font-family:var(--body)}

/* ---------- FRONT ---------- */
.front .sky{position:absolute;left:0;top:0;width:800px;height:246px;background:linear-gradient(160deg,#2d3f5f 0%,var(--navy) 45%,var(--navy-deep) 100%)}
.front .band{position:absolute;left:0;top:248px;width:800px;height:134px;background:linear-gradient(90deg,var(--blue) 0%,#1478c4 60%,var(--blue) 100%);border-top:2px solid #d7e6f3;border-bottom:3px solid #d7e6f3}
.front .hero-ring{position:absolute;left:50px;top:35px;width:332px;height:332px;border-radius:50%;background:#e6e8ea;box-shadow:0 3px 10px rgba(0,0,0,.35)}
.front .hero-photo{position:absolute;left:64px;top:49px;width:304px;height:304px;border-radius:50%;border:3px solid var(--blue);background:radial-gradient(circle at 40% 30%,#d6e6f3 0%,#7fa5c8 40%,#3a4550 75%,#1d2226 100%)}
.brand{position:absolute;left:435px;top:60px;width:320px;color:#fff;font-family:var(--head);font-weight:500;text-align:center}
.brand .brand-top{display:block;font-size:70px;line-height:1;letter-spacing:2px}
.brand .brand-bottom{display:block;font-size:30px;letter-spacing:11px;margin-top:6px}
.front .headline{position:absolute;left:437px;top:268px;color:#fff;font-family:var(--head);font-weight:500;font-size:31px;line-height:42px}
.features{position:absolute;left:0;top:388px;width:800px;height:160px;display:flex;background:linear-gradient(#f2f2f2,#fff 20%)}
.feature{flex:1;text-align:center;padding-top:14px}
.feature .icon{width:64px;height:64px;margin:0 auto;border-radius:50%;background:radial-gradient(circle at 50% 35%,#5a5f66,#2b2e33);border:3px solid #e4e4e4;box-shadow:0 2px 5px rgba(0,0,0,.35);display:flex;align-items:center;justify-content:center}
.feature h3{font-family:var(--head);font-weight:500;font-size:15px;color:var(--ink);margin-top:14px;letter-spacing:.2px}
.feature p{font-size:10.5px;line-height:12px;color:var(--grey);margin-top:5px;padding:0 12px}
.contact-bar{position:absolute;left:0;top:548px;width:800px;height:54px}
.contact-bar .email,.contact-bar .phone{position:absolute;top:16px;color:#fff;font-size:17px;letter-spacing:3px;display:flex;align-items:center;gap:10px}
.contact-bar .email{left:60px}
.contact-bar .phone{left:602px;letter-spacing:1.5px}

/* ---------- BACK ---------- */
.back .masthead{position:absolute;left:0;top:0;width:800px;height:170px;background:linear-gradient(160deg,#2d3f5f 0%,var(--navy) 50%,var(--navy-deep) 100%);border-bottom:3px solid #d7e6f3}
.back .brand{left:55px;top:30px;width:300px}
.back .brand .brand-top{font-size:64px}
.back .brand .brand-bottom{font-size:27px;letter-spacing:10px}
.back .tagline{position:absolute;left:412px;top:40px;font-family:var(--head);font-weight:400;font-size:19px;line-height:26px;color:#fff;width:370px}
.back .tagline .hl{color:var(--cyan)}
.intro{position:absolute;left:0;top:173px;width:398px;height:357px;background:linear-gradient(170deg,#0b5aa2 0%,#1378c5 55%,#1fa0e3 100%);color:#fff;padding:16px 12px 0 38px}
.intro h2{font-family:var(--head);font-weight:500;font-size:15px;letter-spacing:.2px;margin-bottom:16px}
.intro ul{list-style:none}
.intro li{position:relative;padding-left21px;font-size:12.2px;line-height:15px;margin-bottom:12.5px;padding-left:21px}
.intro li::before{content:"›";position:absolute;left:0;top:0;width:12px;height:12px;border:1.3px solid #fff;border-radius:50%;font-size:12px;line-height:9px;text-align:center;font-weight:700}
.signoff{position:absolute;left:40px;top:253px;display:flex;align-items:center;gap:18px}
.signoff .headshot{width:92px;height:92px;border-radius:50%;border:4px solid #e8ecef;background:linear-gradient(160deg,#c9ced4,#7d8690 60%,#3f464e);box-shadow:0 2px 6px rgba(0,0,0,.35)}
.signoff .who{font-size:12.5px;font-weight:700;line-height:16px}
.signoff .reach{font-size:10px;font-weight:400;margin-top:5px;display:flex;gap:12px}
.trial{position:absolute;left:0;top:530px;width:398px;height:72px;background:linear-gradient(90deg,#1b1b1b,#0d0d0d);color:#fff;display:flex;padding:10px 0 0 35px}
.trial h4{font-family:var(--head);font-weight:500;font-size:16px;color:var(--cyan);width:115px;margin-top:-2px}
.trial ul{list-style:none;font-size:11px;line-height:17px}
.trial li{position:relative;padding-left:17px}
.trial li::before{content:"";position:absolute;left:0;top:4px;width:9px;height:9px;border-radius:50%;background:var(--cyan)}
.return-address{position:absolute;left:412px;top:192px;font-size:11px;line-height:13.5px;color:#444}
.indicia{position:absolute;left:692px;top:189px;width:90px;height:90px;border:1px solid #222;font-family:"Arimo",sans-serif;font-size:12px;line-height:14.5px;text-align:center;padding-top:7px;color:#111}
.indicia b{font-weight:700}
.address-block{position:absolute;left:542px;top:347px;width:240px;height:97px;border:1px solid #222;font-family:"Arimo",sans-serif;color:#111}
.address-block .route{position:absolute;right:18px;top:11px;font-size:11px}
.address-block .recipient{position:absolute;left:17px;top:46px;font-size:14.5px;line-height:17px}
</style>
</head>
<body>
<main class="sheet">

  <!-- Side 1 -->
  <div class="card-slot front-slot">
    <section class="card front" aria-label="Postcard front">
      <div class="sky"></div>
      <div class="band"></div>
      <div class="hero-ring"></div>
      <div class="hero-photo" role="img" aria-label="Photo: two climbers on a rocky summit, one helping the other up, against a bright sky"></div>

      <div class="brand"><span class="brand-top">QUIK PATH</span><span class="brand-bottom">PROSPECTS</span></div>

      <h1 class="headline">WE HAVE GREAT TECHNOLOGY<br>THAT CONNECTS PEOPLE</h1>

      <div class="features">
        <div class="feature">
          <div class="icon"><svg width="30" height="30" viewBox="0 0 30 30" fill="#fff"><circle cx="15" cy="10" r="6"/><path d="M4 28c0-7 5-11 11-11s11 4 11 11z"/></svg></div>
          <h3>BEST LEADS, BEST PRICE</h3>
          <p>Our high conversation rates lowers your client acquisition cost<br>Referrals available</p>
        </div>
        <div class="feature">
          <div class="icon"><svg width="36" height="30" viewBox="0 0 36 30" fill="#fff"><circle cx="9" cy="10" r="4"/><circle cx="27" cy="10" r="4"/><circle cx="18" cy="12" r="5"/><path d="M1 24c0-5 4-8 8-8s5 2 5 2v6z"/><path d="M35 24c0-5-4-8-8-8s-5 2-5 2v6z"/><path d="M9 28c0-6 4-9 9-9s9 3 9 9z"/></svg></div>
          <h3>TRUSTED PARTNER</h3>
          <p>Reliability, Dependable, Helpful<br>Deep business &amp; process<br>acumen</p>
        </div>
        <div class="feature">
          <div class="icon"><svg width="28" height="30" viewBox="0 0 28 30"><path d="M14 1l12 4v9c0 8-6 13-12 15C8 27 2 22 2 14V5z" fill="#fff"/><path d="M8 15l4 4 8-8" stroke="#2b2e33" stroke-width="3" fill="none"/></svg></div>
          <h3>HIGH VOLUME, QUALITY LEADS</h3>
          <p>50 years of SSD domain<br>knowledge tested technology<br>capabilities</p>
        </div>
        <div class="feature">
          <div class="icon"><svg width="34" height="32" viewBox="0 0 34 32" fill="none" stroke="#fff"><circle cx="13" cy="19" r="7" stroke-width="5" stroke-dasharray="3 2.5"/><circle cx="13" cy="19" r="3" stroke-width="2"/><circle cx="25" cy="9" r="5" stroke-width="4" stroke-dasharray="2.4 2"/><circle cx="25" cy="9" r="2" stroke-width="1.5"/></svg></div>
          <h3>EASY TO USE</h3>
          <p>Integrate seamlessly into your<br>IT systems<br>Tailored campaigns</p>
        </div>
      </div>

      <div class="contact-bar">
        <svg width="800" height="54" viewBox="0 0 800 54" style="position:absolute;left:0;top:0">
          <defs>
            <linearGradient id="barDark" x1="0" x2="1"><stop offset="0" stop-color="#222"/><stop offset="1" stop-color="#0b0b0b"/></linearGradient>
            <linearGradient id="barBlue" x1="0" x2="1"><stop offset="0" stop-color="#0a4f8c"/><stop offset=".6" stop-color="#1479c6"/><stop offset="1" stop-color="#0a4f8c"/></linearGradient>
          </defs>
          <rect width="800" height="54" fill="url(#barDark)"/>
          <polygon points="520,54 560,0 800,0 800,54" fill="url(#barBlue)"/>
          <polygon points="498,54 538,0 548,0 508,54" fill="#fff"/>
        </svg>
        <span class="email"><svg width="16" height="14" viewBox="0 0 16 14" fill="none" stroke="#fff" stroke-width="1.6"><path d="M1 6l7-5 7 5v7H1z"/><path d="M1 6l7 4 7-4"/></svg>Warren@QuikPathProspects.com</span>
        <span class="phone"><svg width="14" height="14" viewBox="0 0 14 14" fill="#fff"><path d="M3 1l2 3-1.5 1.5c.8 2 2.2 3.4 4 4L9 8l3 2-1 3C6 13 1 8 1 3z"/></svg>555-014-2276</span>
      </div>
    </section>
  </div>

  <!-- Side 2 -->
  <div class="card-slot back-slot">
    <section class="card back" aria-label="Postcard back">
      <div class="masthead"></div>
      <div class="brand"><span class="brand-top">QUIK PATH</span><span class="brand-bottom">PROSPECTS</span></div>
      <p class="tagline"><span class="hl">BEST LEADS …</span> BEST PRICE WITH HIGH VOLUME &amp; QUALITY CAPACITY … <span class="hl">LEADS FROM A TRUSTED PARTNER THAT IS EASY TO USE</span></p>

      <div class="intro">
        <h2>I WANT TO PERSONALLY INTRODUCE OUR COMPANY TO YOU!</h2>
        <ul>
          <li>My team as &gt; 50 years of cumulative SSD experience.</li>
          <li>We have proven technology that delivers the best leads.</li>
          <li>The timing is right for a new competitor in this industry.</li>
          <li>I had to come out of retirement after 30 years with Norvell, the opportunity is just that great … I love building businesses and partnering with great customers!</li>
          <li>Our business, industry, &amp; technical acumen is unrivaled… and we can do it at a cost than no others can.</li>
        </ul>
        <div class="signoff">
          <div class="headshot" role="img" aria-label="Portrait photo of Warren Beckett, President"></div>
          <div class="who">Warren Beckett<br>President, Quik Path Prospects
            <div class="reach"><span>&#9742; 555-014-2276</span><span>&#9993; Warren@QuikPathProspects.com</span></div>
          </div>
        </div>
      </div>

      <div class="trial">
        <h4>TEST OUR LEADS</h4>
        <ul>
          <li>Start at 250 or 500 Leads.</li>
          <li>Grow to 1,000 … 3,000 or even 10,000!</li>
          <li>We give the right support to your growth.</li>
        </ul>
      </div>

      <address class="return-address" style="font-style:normal">
        Warren Beckett, President Quik Path Prospects<br>
        1250 Ridgeline Avenue, Suite 400<br>
        Dayton OH 45402<br>
        555-014-2276<br>
        Warren@QuikPathProspects.com
      </address>

      <div class="indicia">PRSRT STD<br>ECRWSS<br>U.S. Postage<br><b>PAID</b><br>EDDM RETAIL</div>

      <div class="address-block">
        <span class="route">*****************ECRWSS****</span>
        <span class="recipient">Local<br>Postal Customer</span>
      </div>
    </section>
  </div>

</main>
</body>
</html>
```